Technology Solutions Provider

Let’s design a business card that will be as simple and bold at the same time. Name, email address, website & phone number.

Target Market(s)

Small to Medium Size Business

Industry/Entity Type

It Professional

Contact Information for Business Card

Name, email, website, phone numbers

Font styles to use
Sans Serif

Colors
ec1f27
f04a50
dddddd
919191
000000
ffffff

Requirements
Must have
• Clean simple look using my existing logo. I just need to the basic contact information on this card.
Nice to have
• Im considering the square size card versus the standard size business card.
Should not have
• No Mailing Address, no list of services.

```html
<!DOCTYPE html>
<html lang="en">
<head>
<meta charset="utf-8">
<title>Kestrel Networks – Square Business Card</title>
<link rel="stylesheet" href="https://fonts.googleapis.com/css2?family=Source+Sans+3:wght@400;600;700&display=swap">
<style>
  :root {
    --red: #ec1f27;
    --red-soft: #f04a50;
    --light: #dddddd;
    --grey: #919191;
    --black: #000000;
    --white: #ffffff;
    --card-face: #f2f2f2;
    --stage: #333333;
    --ink: #1a1a1a;
  }
  * { margin: 0; padding: 0; box-sizing: border-box; }
  html, body {
    width: 1200px;
    height: 900px;
    overflow: hidden;
    background: var(--stage);
    font-family: "Source Sans 3", "Helvetica Neue", Arial, sans-serif;
  }
  .canvas {
    position: relative;
    width: 1200px;
    height: 900px;
  }
  .card {
    position: absolute;
    top: 281px;
    width: 347px;
    height: 338px;
  }
  .card--front {
    left: 259px;
    background: var(--card-face);
    text-align: center;
  }
  .card--back {
    left: 659px;
    background: var(--red);
    overflow: hidden;
  }
  .brand {
    position: absolute;
    left: 0;
    right: 0;
    display: flex;
    align-items: center;
    justify-content: center;
    gap: 8px;
    font-weight: 600;
    font-size: 30px;
    letter-spacing: 0.2px;
    line-height: 1;
  }
  .brand__dot {
    width: 12px;
    height: 12px;
    border-radius: 50%;
    flex: none;
  }
  .card--front .brand { top: 64px; color: var(--red); }
  .card--front .brand__dot { background: var(--red); }
  .card--back .brand { top: 152px; color: var(--white); }
  .card--back .brand__dot { background: var(--white); }
  .back-texture {
    position: absolute;
    inset: 0;
    display: block;
  }
  .holder {
    position: absolute;
    top: 150px;
    left: 0;
    right: 0;
  }
  .holder__name {
    color: var(--red);
    font-weight: 700;
    font-size: 23px;
    letter-spacing: 0.2px;
    line-height: 1.1;
  }
  .holder__title {
    color: var(--ink);
    font-size: 15.5px;
    margin-top: 3px;
  }
  .divider {
    position: absolute;
    top: 217px;
    left: 100px;
    width: 147px;
    height: 1px;
    background: var(--red);
    border: 0;
  }
  .contact {
    position: absolute;
    top: 237px;
    left: 0;
    right: 0;
    list-style: none;
    font-size: 15.5px;
    line-height: 21px;
    color: var(--ink);
  }
  .contact__label {
    color: var(--red);
    font-weight: 700;
  }
  .contact__web {
    color: var(--red);
    font-weight: 700;
  }
</style>
</head>
<body>
  <main class="canvas">
    <section class="card card--front" aria-label="Business card front">
      <div class="brand">
        <span class="brand__dot"></span>
        <span class="brand__name">Kestrel Networks</span>
      </div>
      <div class="holder">
        <p class="holder__name">JOHN SMITH</p>
        <p class="holder__title">Managing Director</p>
      </div>
      <hr class="divider">
      <ul class="contact">
        <li><span class="contact__label">P:</span> 823-456-7890</li>
        <li><span class="contact__label">E:</span> info@youremail.com</li>
        <li class="contact__web">www.websitename.com</li>
      </ul>
    </section>

    <section class="card card--back" aria-label="Business card back">
      <svg class="back-texture" width="347" height="338" viewBox="0 0 347 338" role="img" aria-label="Subtle diagonal repeating brand-name pattern on red">
        <defs>
          <linearGradient id="backTone" x1="0" y1="0" x2="1" y2="1">
            <stop offset="0" stop-color="#ec1f27"/>
            <stop offset="0.5" stop-color="#e2262d"/>
            <stop offset="1" stop-color="#ec1f27"/>
          </linearGradient>
        </defs>
        <rect width="347" height="338" fill="url(#backTone)"/>
      </svg>
      <div class="brand">
        <span class="brand__dot"></span>
        <span class="brand__name">Kestrel Networks</span>
      </div>
    </section>
  </main>
</body>
</html>
```